Business Card Design

We are a florist shop that also stocks a range of giftware and jewellery. I would like a new design that incorporates a light green background. If you could use a skeleton leaf somewhere in the design that would be great. I would also like to incorporate the find us on Chatterlink logo on this design.

Industry/Entity Type

Florist

Contact Information for Business Card

Petals at Harwick
42 Tellbury street
Wendmoor Calder 3918
Phone: 0352984407
Fax : 0352984433
email: pah@brightmail.net.au

Proprietors : Dana & Lou Fenwright

```html
<!DOCTYPE html>
<html lang="en">
<head>
<meta charset="utf-8">
<title>Petals at Harwick – Business Card</title>
<link href="https://fonts.googleapis.com/css2?family=Macondo&family=Mulish:wght@400;700&display=swap" rel="stylesheet">
<style>
  :root {
    --card-green: #c9e2bf;
    --leaf-light: #eef6d8;
    --leaf-mid: #d6ebb4;
    --ink: #1c1c1c;
    --social-tile: #7f9c74;
    --title-white: #ffffff;
    --title-shadow: rgba(60, 70, 55, 0.55);
  }
  html, body {
    margin: 0;
    padding: 0;
    width: 1200px;
    height: 761px;
    overflow: hidden;
    background: #ffffff;
  }
  .business-card {
    position: relative;
    width: 1200px;
    height: 761px;
    background: var(--card-green);
    overflow: hidden;
    font-family: "Mulish", "Avenir", sans-serif;
    color: var(--ink);
  }
  .leaf-artwork {
    position: absolute;
    background: radial-gradient(ellipse at center, var(--leaf-light) 0%, var(--leaf-mid) 45%, rgba(201, 226, 191, 0) 72%);
  }
  .leaf-artwork--bottom-left { left: -40px; top: 270px; width: 440px; height: 520px; }
  .leaf-artwork--top-right { left: 930px; top: -40px; width: 310px; height: 460px; }
  .shop-name {
    position: absolute;
    left: 36px;
    top: 62px;
    margin: 0;
    font-family: "Macondo", "Papyrus", fantasy;
    font-weight: 400;
    color: var(--title-white);
    text-shadow: 3px 4px 5px var(--title-shadow);
    white-space: nowrap;
    line-height: 1;
  }
  .shop-name__main { font-size: 168px; }
  .shop-name__rest { font-size: 82px; margin-left: 18px; }
  .card-line {
    position: absolute;
    left: 451px;
    margin: 0;
    line-height: 1;
    white-space: nowrap;
  }
  .proprietors { top: 316px; font-size: 36px; }
  .contact__address { top: 439px; font-size: 34px; }
  .contact__phones { top: 503px; font-size: 34px; }
  .contact__email { top: 548px; font-size: 34px; }
  .contact__label { font-weight: 700; }
  .contact__gap { display: inline-block; width: 40px; }
  .social-link {
    position: absolute;
    left: 448px;
    top: 617px;
    display: flex;
    align-items: center;
    gap: 22px;
    color: var(--ink);
    font-weight: 700;
  }
  .social-link__square {
    width: 71px;
    height: 71px;
    background: var(--social-tile);
  }
  .social-link__text { line-height: 1; }
  .social-link__lead { display: block; font-size: 28px; margin-bottom: 4px; }
  .social-link__name { display: block; font-size: 40px; }
</style>
</head>
<body>
  <div class="business-card">
    <div class="leaf-artwork leaf-artwork--bottom-left" role="img" aria-label="Pale green skeleton leaves overlapping in the lower left corner"></div>
    <div class="leaf-artwork leaf-artwork--top-right" role="img" aria-label="Pale green skeleton leaves in the upper right corner"></div>

    <h1 class="shop-name"><span class="shop-name__main">Petals</span><span class="shop-name__rest">at Harwick</span></h1>

    <p class="card-line proprietors">Dana &amp; Lou Fenwright</p>

    <p class="card-line contact__address">42 Tellbury street Wendmoor Calder 3918</p>
    <p class="card-line contact__phones"><span class="contact__label">P.</span> 0352984407<span class="contact__gap"></span><span class="contact__label">F.</span> 0352984433</p>
    <p class="card-line contact__email"><span class="contact__label">E.</span> pah@brightmail.net.au</p>

    <div class="social-link">
      <span class="social-link__square"></span>
      <span class="social-link__text">
        <span class="social-link__lead">Find us on</span>
        <span class="social-link__name">Chatterlink</span>
      </span>
    </div>
  </div>
</body>
</html>
```